Book cover

I am working with my publisher to publish my book They came up with a book cover but I don't like it. I want to see different designs. The book Title is Shiftcraftery the subtitle How to Steer Upheaval with Focus, Poise & Resolve by Marilyn T. Hargreave
I want to use my Brand Colors including the blue. I am uploading the covers of my other book. This is a professional leadership book. The publisher will make the cover when providing them a new design. the Shiftcraftery one is one I played with on Canva. I would like more color and to incorporate the blue. I want a spot at the top where I can write a quote. Shiftcraftery is one word in the text so should be the same on the cover. I want the cover to show energy movement and am open to an image too. I am attaching logos for the feel of the brand and brand rgb codes.

```html
<!DOCTYPE html>
<html lang="en">
<head>
<meta charset="utf-8">
<title>Shiftcraftery — Book Cover</title>
<link rel="stylesheet" href="https://fonts.googleapis.com/css2?family=Montserrat:wght@400;600;700&family=Saira+Extra+Condensed:wght@700&family=Merriweather:wght@900&display=swap">
<style>
  :root {
    --backdrop: #5e5e5e;
    --teal-deep: #1d6a70;
    --teal: #3aa6ab;
    --teal-light: #8fd3d5;
    --ice: #eef3f5;
    --title-white: #f4f6f7;
    --accent-red: #e8402f;
    --band: #1b1b1b;
    --band-text: #f2f2f2;
  }
  * { margin: 0; padding: 0; box-sizing: border-box; }
  html, body {
    width: 980px;
    height: 1200px;
    overflow: hidden;
    background: var(--backdrop);
  }
  .cover {
    position: absolute;
    left: 80px;
    top: 20px;
    width: 820px;
    height: 1160px;
    overflow: hidden;
    background: var(--ice);
  }
  .cover-art {
    position: absolute;
    inset: 0 0 168px 0;
    background:
      radial-gradient(ellipse 70% 30% at 70% 8%, var(--ice) 0%, rgba(238,243,245,0) 70%),
      radial-gradient(ellipse 85% 32% at 40% 78%, var(--ice) 40%, rgba(238,243,245,0) 75%),
      radial-gradient(ellipse 80% 28% at 60% 30%, var(--teal-deep) 10%, rgba(29,106,112,0) 80%),
      linear-gradient(180deg, var(--teal-light) 0%, var(--teal) 25%, var(--teal) 55%, var(--teal-light) 68%, var(--ice) 82%, var(--ice) 100%);
  }
  .tagline {
    position: absolute;
    left: 69px;
    top: 120px;
    font-family: "Montserrat", sans-serif;
    font-weight: 700;
    font-size: 16px;
    line-height: 22px;
    color: var(--title-white);
    text-transform: uppercase;
    letter-spacing: 0.2px;
  }
  .title {
    position: absolute;
    left: 0;
    top: 270px;
    width: 820px;
    height: 200px;
  }
  .title text {
    font-family: "Saira Extra Condensed", sans-serif;
    font-weight: 700;
    font-size: 232px;
  }
  .title .word-lead { fill: var(--title-white); }
  .title .word-tail { fill: var(--accent-red); }
  .subtitle {
    position: absolute;
    left: 0;
    top: 710px;
    width: 880px;
    text-align: center;
    font-family: "Montserrat", sans-serif;
    color: var(--accent-red);
  }
  .subtitle-lead {
    display: block;
    font-weight: 400;
    font-size: 26px;
    line-height: 34px;
  }
  .subtitle-virtues {
    display: block;
    font-weight: 600;
    font-size: 26px;
    line-height: 34px;
    text-transform: uppercase;
  }
  .author-band {
    position: absolute;
    left: 0;
    bottom: 0;
    width: 820px;
    height: 168px;
    background: var(--band);
    display: flex;
    align-items: center;
    justify-content: center;
  }
  .author {
    font-family: "Merriweather", serif;
    font-weight: 900;
    font-size: 35px;
    color: var(--band-text);
    text-transform: uppercase;
    padding-left: 60px;
    letter-spacing: 0.5px;
  }
</style>
</head>
<body>
  <main class="cover">
    <div class="cover-art" role="img" aria-label="Abstract teal and white watercolour flow with icy layered waves"></div>

    <p class="tagline">Shiftcraftery is the essential playbook<br>to turn your uncertainty into possibility</p>

    <svg class="title" viewBox="0 0 820 200" aria-label="Shiftcraftery" role="heading">
      <defs>
        <filter id="title-lift" x="-5%" y="-10%" width="110%" height="130%">
          <feDropShadow dx="0" dy="5" stdDeviation="4" flood-color="#0c3a3e" flood-opacity="0.55"/>
        </filter>
      </defs>
      <text x="60" y="186" textLength="726" lengthAdjust="spacingAndGlyphs" filter="url(#title-lift)"><tspan class="word-lead">SHIFT</tspan><tspan class="word-tail">CRAFTERY</tspan></text>
    </svg>

    <p class="subtitle">
      <span class="subtitle-lead">How to Steer Upheaval with</span>
      <span class="subtitle-virtues">Focus, Poise &amp; Resolve</span>
    </p>

    <footer class="author-band">
      <p class="author">Marilyn T. Hargreave</p>
    </footer>
  </main>
</body>
</html>
```